brightwave pools cards

i need to create a design to use on my business cards,brochures and as a letterhead. i am a new swimming pool renovation business named BRIGHTWAVE POOLS. I require a smart professional deign to reflect that my business is the best in the industry.
should include something like.... Brightwave Pools ABN - 57184620931
residential pool renovation specialists
specialising in the art of - fully tiled pools
- waterline tiles
- natural stone pool copings
and outdoor areas - concrete slabs - detailed mosaic work - pool lighting and water features - pool painting

trent - 0461829304 gordon -0438152967 brightwavepoolsnorth@mailbox-example.com

the design could feature - water, natural stone (travertine, sandstone etc), something to personafy the word imagine.
looking foward to seeing some ideas... cheers heaps trent

```html
<!DOCTYPE html>
<html lang="en">
<head>
<meta charset="utf-8">
<title>Brightwave Pools – Business Card</title>
<link rel="stylesheet" href="https://fonts.googleapis.com/css2?family=Arimo:wght@400;700&display=swap">
<style>
  :root {
    --card-bg: #ffffff;
    --ink-heading: #1a4fc4;
    --ink-body: #2058d2;
  }
  html, body {
    margin: 0;
    padding: 0;
    overflow: hidden;
    background: var(--card-bg);
  }
  .card {
    position: relative;
    width: 1200px;
    height: 750px;
    background: var(--card-bg);
    font-family: "Arimo", Arial, sans-serif;
    overflow: hidden;
  }
  .business-name {
    position: absolute;
    left: 78px;
    top: 54px;
    margin: 0;
    font-size: 39px;
    font-weight: 700;
    line-height: 48px;
    color: var(--ink-heading);
    letter-spacing: 0.6px;
    white-space: nowrap;
    transform: scaleX(1.3);
    transform-origin: left top;
  }
  .services,
  .contact {
    position: absolute;
    left: 78px;
    margin: 0;
    padding: 0;
    list-style: none;
    font-size: 37px;
    font-weight: 400;
    line-height: 37.5px;
    color: var(--ink-body);
    white-space: nowrap;
    transform: scaleX(1.3);
    transform-origin: left top;
  }
  .services li,
  .contact li {
    display: block;
    height: 37.5px;
  }
  .services { top: 137px; }
  .services .indent { padding-left: 24px; }
  .contact-primary { top: 551px; }
  .contact-secondary { top: 624px; }
</style>
</head>
<body>
  <main class="card">
    <h1 class="business-name">Brightwave Pools ABN - 57184620931</h1>
    <ul class="services">
      <li>residential pool renovation specialists</li>
      <li>specialising in the art of</li>
      <li>- fully tiled pools</li>
      <li>- waterline tiles</li>
      <li>- natural stone pool copings</li>
      <li class="indent">and outdoor areas</li>
      <li>- concrete slabs</li>
      <li>- detailed mosaic work</li>
      <li>- pool lighting and water features</li>
      <li>- pool painting</li>
    </ul>
    <ul class="contact contact-primary">
      <li>trent - 0461829304</li>
    </ul>
    <ul class="contact contact-secondary">
      <li>gordon -0438152967</li>
      <li>brightwavepoolsnorth@mailbox-example.com</li>
    </ul>
  </main>
</body>
</html>
```